Evergrove Yard Service and Beyond LLC

• Mowing
• Weed eating
•Edging
• hedge trimming
• landscaping
•mulching
•yard clean up
• pressure washing

Target Market(s)

Everyone

Contact Information for Business Card

Licensed and insured

Font styles to use
Serif

Colors
59FF00
82FF00
B8FF75
E3FFCB
F4FFEA
F0912C
F2A743
F7CA91
FBE8D2
FDF5EE
EE7325
F08F49
F5BC92
FAE3D3
FDF4ED
EB3D1F
EC4F4E
F09395
F8D3D4
FCEDEE
E54698
E96AAD
F1A4CE
F9D9EA
FCEFF6

```html
<!DOCTYPE html>
<html lang="en">
<head>
<meta charset="utf-8">
<title>Evergrove Yard Service and Beyond LLC – Business Card</title>
<link href="https://fonts.googleapis.com/css2?family=Poppins:wght@700&family=Questrial&display=swap" rel="stylesheet">
<style>
  :root {
    --leaf-green: #8dc63f;
    --leaf-green-pale: #cfe8a9;
    --leaf-green-soft: #b2d97a;
    --ember-orange: #f15a2b;
    --ink: #231f20;
    --paper: #ffffff;
    --card-edge: #3a3a3a;
  }
  * { margin: 0; padding: 0; box-sizing: border-box; }
  html, body {
    width: 1200px;
    height: 616px;
    overflow: hidden;
    background: var(--paper);
  }
  .canvas {
    position: relative;
    width: 1200px;
    height: 616px;
    font-family: "Questrial", sans-serif;
  }
  .card {
    position: absolute;
    top: 166px;
    width: 507px;
    height: 286px;
    border: 1px solid var(--card-edge);
    box-shadow: 1px 2px 4px rgba(0,0,0,0.18);
    overflow: hidden;
  }
  .card--front { left: 92px; background: var(--paper); }
  .card--back  { left: 616px; background: var(--leaf-green); }

  /* Front */
  .seedling-art {
    position: absolute;
    left: 66px;
    top: 50px;
    width: 110px;
    height: 176px;
    border-radius: 55px 55px 8px 8px;
    background: linear-gradient(180deg, var(--leaf-green-soft) 0%, var(--leaf-green-pale) 100%);
  }
  .ground-line {
    position: absolute;
    left: 0;
    top: 225px;
    width: 415px;
    height: 2px;
    background: var(--leaf-green);
  }
  .accent-band {
    position: absolute;
    left: 444px;
    top: 168px;
    width: 63px;
    height: 26px;
    background: var(--ember-orange);
  }
  .business-name {
    position: absolute;
    left: 242px;
    top: 160px;
    font-family: "Poppins", sans-serif;
    font-weight: 700;
    color: var(--ember-orange);
    line-height: 1;
    white-space: nowrap;
  }
  .business-name__primary {
    display: block;
    font-size: 36px;
    letter-spacing: -1px;
  }
  .business-name__secondary {
    display: block;
    margin-top: 2px;
    font-size: 15.5px;
    letter-spacing: -0.4px;
  }
  .business-name__suffix {
    position: absolute;
    left: 421px;
    top: 215px;
    font-family: "Poppins", sans-serif;
    font-weight: 700;
    font-size: 10px;
    color: var(--ember-orange);
  }
  .tagline {
    position: absolute;
    left: 242px;
    top: 230px;
    font-size: 14.5px;
    letter-spacing: 1.7px;
    color: var(--ink);
    white-space: nowrap;
  }

  /* Back */
  .service-list {
    position: absolute;
    left: 74px;
    top: 48px;
    list-style: none;
    color: var(--paper);
    font-size: 14.5px;
    line-height: 23.8px;
    text-transform: uppercase;
  }
  .service-list li::before {
    content: "•";
    display: inline-block;
    width: 10px;
    font-size: 11px;
  }
  .seedling-art--reverse {
    left: 320px;
    top: 60px;
    width: 152px;
    height: 226px;
    border-radius: 76px 76px 0 0;
    background: linear-gradient(180deg, rgba(255,255,255,0.55) 0%, rgba(255,255,255,0.3) 100%);
  }
</style>
</head>
<body>
<main class="canvas">
  <section class="card card--front" aria-label="Card front">
    <div class="seedling-art" role="img" aria-label="Green seedling illustration rising from the ground line"></div>
    <div class="business-name">
      <span class="business-name__primary">Evergrove</span>
      <span class="business-name__secondary">Yard Service and Beyond</span>
    </div>
    <span class="business-name__suffix">LLC</span>
    <div class="accent-band"></div>
    <div class="ground-line"></div>
    <p class="tagline">Licensed and insured</p>
  </section>

  <section class="card card--back" aria-label="Card back">
    <ul class="service-list">
      <li>Mowing</li>
      <li>Weed Eating</li>
      <li>Edging</li>
      <li>Hedge Trimming</li>
      <li>Landscaping</li>
      <li>Mulching</li>
      <li>Yard Clean Up</li>
      <li>Pressure Washing</li>
    </ul>
    <div class="seedling-art seedling-art--reverse" role="img" aria-label="Large white seedling illustration"></div>
  </section>
</main>
</body>
</html>
```